Personal Brand Business Card

I am looking for a design that I will use as my personal brand that conveys class (think 1920s gentlemen) and is timeless. I will be putting this on a pearl white, letter pressed, cotton business card.  I’m thinking maybe something with my initials on the front they will flip over for the rest of my information.  But don’t let that limit you.
The information I will have on the back of the business card will be my name, email, and phone number.
Some of the attributes that best describe me are: loyal, dependable, creative, risk taker, open minded, competitive, and empathetic.  I can adapt to my environment quickly and can get along with anyone.  I get excited by figuring out the way things work and finding solutions to problems.

Industry/Entity Type
Business

```html
<!DOCTYPE html>
<html lang="en">
<head>
<meta charset="utf-8">
<title>Grant Whitcombe – Business Card</title>
<link rel="stylesheet" href="https://fonts.googleapis.com/css2?family=Cinzel:wght@400&family=Arimo:wght@400&display=swap">
<style>
  :root {
    --backdrop: #b9babc;
    --card: #ffffff;
    --ink: #111111;
    --ink-soft: #555555;
    --icon: #4a4a4a;
  }
  * { margin: 0; padding: 0; box-sizing: border-box; }
  html, body {
    width: 1200px;
    height: 1200px;
    overflow: hidden;
    background: var(--backdrop);
  }
  .canvas {
    position: relative;
    width: 1200px;
    height: 1200px;
  }
  .card {
    position: absolute;
    width: 660px;
    height: 377px;
    background: var(--card);
  }
  .card--info { left: 124px; top: 184px; }
  .card--mark {
    left: 415px;
    top: 624px;
    display: flex;
    align-items: center;
    justify-content: center;
  }
  .identity {
    position: absolute;
    top: 88px;
    left: 0;
    width: 100%;
    text-align: center;
  }
  .identity__name {
    font-family: "Cinzel", serif;
    font-weight: 400;
    font-size: 30px;
    letter-spacing: 1px;
    color: var(--ink);
    line-height: 1;
  }
  .identity__title {
    margin-top: 12px;
    font-family: "Arimo", sans-serif;
    font-size: 21px;
    letter-spacing: 1px;
    color: var(--ink-soft);
    line-height: 1;
  }
  .contact {
    position: absolute;
    left: 57px;
    top: 226px;
    list-style: none;
  }
  .contact__item {
    display: flex;
    align-items: center;
    height: 38px;
    margin-bottom: 6px;
    font-family: "Arimo", sans-serif;
    font-size: 23px;
    color: var(--ink);
  }
  .contact__icon {
    width: 42px;
    height: 34px;
    margin-right: 16px;
    flex: none;
  }
  .brand-name {
    font-family: "Cinzel", serif;
    font-weight: 400;
    font-size: 54px;
    line-height: 1;
    letter-spacing: 2px;
    color: var(--ink);
    white-space: nowrap;
  }
</style>
</head>
<body>
  <main class="canvas">
    <section class="card card--info">
      <header class="identity">
        <h1 class="identity__name">GRANT WHITCOMBE</h1>
        <p class="identity__title">CONSULTANT</p>
      </header>
      <ul class="contact">
        <li class="contact__item">
          <svg class="contact__icon" viewBox="0 0 42 34" aria-hidden="true">
            <rect x="2" y="5" width="38" height="24" rx="2" fill="none" stroke="var(--icon)" stroke-width="2"/>
            <path d="M3 6 L21 20 L39 6 M3 28 L16 16 M39 28 L26 16" fill="none" stroke="var(--icon)" stroke-width="2"/>
          </svg>
          <span>grant.whitcombe@example.com</span>
        </li>
        <li class="contact__item">
          <svg class="contact__icon" viewBox="0 0 42 34" aria-hidden="true">
            <path d="M8 3 C5 5 4 9 6 14 C10 23 17 29 26 32 C31 33 34 31 36 28 L30 22 C28 23 26 25 24 24 C19 21 15 17 13 12 C12 10 14 8 15 7 Z" fill="none" stroke="var(--icon)" stroke-width="2" stroke-linejoin="round"/>
          </svg>
          <span>215-555-0148</span>
        </li>
      </ul>
    </section>

    <section class="card card--mark">
      <p class="brand-name">GRANT WHITCOMBE</p>
    </section>
  </main>
</body>
</html>
```